Ferncrest Dental, LLC business card project

Business card to be designed with current logo.
Dental office- please keep design of card that looks clean and professional.
Please include the following info:
Ferncrest Dental, LLC
Dr. Lorna Pettigrew
2871 Marlowe Street
Bethlehem, PA 18093
610-555-0193
ferncrestdental.office@examplemail.test
Hello everyone-
Reason: Just got back from overseas- will look at all designs and provide feedback. Thank you!
Reason: Polling my friends for the final selection-
thank you to all those that participated- so many talented designers!

```html
<!DOCTYPE html>
<html lang="en">
<head>
<meta charset="utf-8">
<title>Ferncrest Dental — Business Card</title>
<link rel="stylesheet" href="https://fonts.googleapis.com/css2?family=Arimo:wght@400;700&display=swap">
<style>
  :root {
    --backdrop: #3b3e3b;
    --card: #fbfbfa;
    --green-deep: #5c8f2f;
    --green-leaf: #9cc431;
    --green-rule: #c9dd8a;
    --text-font: "Arimo", Arial, sans-serif;
  }
  * { box-sizing: border-box; margin: 0; padding: 0; }
  html, body {
    width: 1200px; height: 900px; overflow: hidden;
    background: var(--backdrop);
    font-family: var(--text-font);
  }
  .canvas {
    position: relative; width: 1200px; height: 900px;
    display: flex; flex-direction: column; align-items: center; justify-content: center; gap: 48px;
  }
  .card {
    position: relative; width: 640px; height: 366px;
    background: var(--card);
    box-shadow: 0 6px 18px rgba(0,0,0,.35);
  }
  .brand {
    display: flex; align-items: center; gap: 12px;
    color: var(--green-deep); font-weight: 400; letter-spacing: .01em;
  }
  .brand-dot { border-radius: 50%; background: var(--green-leaf); flex: none; }

  /* front */
  .card-front .brand { position: absolute; left: 48px; top: 40px; font-size: 34px; }
  .card-front .brand-dot { width: 26px; height: 26px; }
  .holder {
    position: absolute; left: 48px; top: 162px; width: 440px;
    font-size: 21px; font-weight: 700; color: var(--green-leaf);
    padding-bottom: 8px; border-bottom: 1.5px solid var(--green-rule);
  }
  .details {
    position: absolute; left: 56px; top: 222px;
    font-size: 15px; line-height: 19px; color: var(--green-deep);
  }
  .details .company { font-weight: 700; }
  .contact-row { display: flex; align-items: center; gap: 22px; margin-top: 10px; }
  .contact-item { display: flex; align-items: center; gap: 6px; }
  .contact-item svg { flex: none; }

  /* back */
  .card-back { display: flex; align-items: center; justify-content: center; }
  .card-back .brand { font-size: 48px; gap: 16px; }
  .card-back .brand-dot { width: 36px; height: 36px; }
</style>
</head>
<body>
<main class="canvas">
  <section class="card card-front" aria-label="Business card front">
    <div class="brand"><span class="brand-dot"></span><span class="brand-name">FerncrestDental</span></div>
    <h1 class="holder">Dr. Lorna Pettigrew</h1>
    <div class="details">
      <p class="company">Ferncrest Dental, LLC</p>
      <p>2871 Marlowe Street</p>
      <p>Bethlehem, PA 18093</p>
      <div class="contact-row">
        <span class="contact-item">
          <svg width="12" height="12" viewBox="0 0 12 12" aria-hidden="true">
            <circle cx="6" cy="6" r="6" fill="var(--green-deep)"/>
            <path d="M3.6 3.2c.4-.4.8-.3 1 .1l.5.9c.2.3.1.6-.2.8l-.3.2c.3.8.9 1.4 1.7 1.7l.2-.3c.2-.3.5-.4.8-.2l.9.5c.4.2.5.6.1 1-.6.6-1.4.7-2.2.3C4.9 7.6 4.4 7.1 3.8 5.6c-.4-.9-.8-1.8-.2-2.4z" fill="var(--card)"/>
          </svg>
          610-555-0193
        </span>
        <span class="contact-item">
          <svg width="13" height="10" viewBox="0 0 13 10" aria-hidden="true">
            <rect x=".6" y=".6" width="11.8" height="8.8" rx="1" fill="none" stroke="var(--green-deep)" stroke-width="1.2"/>
            <path d="M1 1.2l5.5 4.2L12 1.2" fill="none" stroke="var(--green-deep)" stroke-width="1.2"/>
          </svg>
          ferncrestdental.office@examplemail.test
        </span>
      </div>
    </div>
  </section>

  <section class="card card-back" aria-label="Business card back">
    <div class="brand"><span class="brand-dot"></span><span class="brand-name">FerncrestDental</span></div>
  </section>
</main>
</body>
</html>
```